Online Travel Agency card design with 2 logos

Need a two sided business card design for online tourism agency which is based in Istanbul Turkey.
Need a business card design where it shows the travel agency logo but also the logo and information of the parent company as well.Parent company logo is just text with 2 different colors. (Arial font with text TemaVista "Tema"- hex #172841 and "Vista" hex-#FF7F00)
Both logos are uploaded.
Target Market(s)
travel , online
Industry/Entity Type
Travel
Contact Information for Business Card
The information on the card should be as :
Travel Agency Logo logo (rnlogo)
Parent Company logo(temalogo)
Company information :TemaVista Turizm ve Bilgi Teknolojileri A.Ş
Address of company
Tel
Email
Name
Position(english and turkish)
Look and feel
Each slider illustrates characteristics of the customer's brand and the style your logo design should communicate.

```html
<!DOCTYPE html>
<html lang="tr">
<head>
<meta charset="utf-8">
<title>rotanokta – Business Card</title>
<link href="https://fonts.googleapis.com/css2?family=Arimo:wght@400;700&display=swap" rel="stylesheet">
<style>
  :root {
    --backdrop: #64a7bb;
    --paper: #f4f5f6;
    --navy: #172841;
    --sky: #7cc3de;
    --orange: #ff7f00;
    --ink: #1f2630;
  }
  * { margin: 0; padding: 0; box-sizing: border-box; }
  html, body { width: 1200px; height: 814px; overflow: hidden; }
  body {
    background: var(--backdrop);
    font-family: "Arimo", Arial, sans-serif;
    position: relative;
  }
  .card {
    position: absolute;
    top: 252px;
    width: 540px;
    height: 309px;
    background: var(--paper);
    overflow: hidden;
    box-shadow: 0 10px 24px rgba(20, 50, 65, 0.25);
  }
  .card--front { left: 40px; }
  .card--back { left: 620px; }

  /* front side */
  .front-brand {
    position: absolute;
    left: 0; right: 0; top: 70px;
    display: flex;
    flex-direction: column;
    align-items: center;
  }
  .brand-disc {
    width: 118px; height: 118px;
    border-radius: 50%;
    background: var(--navy);
  }
  .parent-name {
    margin-top: 8px;
    font-size: 12px;
    font-weight: 700;
    color: var(--navy);
    align-self: center;
    transform: translateX(48px);
  }
  .brand-name {
    font-size: 34px;
    font-weight: 700;
    color: var(--navy);
    letter-spacing: -0.5px;
    line-height: 1;
  }

  /* back side */
  .back-panel { position: absolute; left: 0; top: 0; }
  .back-brand {
    position: absolute;
    left: 38px; bottom: 30px;
    color: #ffffff;
  }
  .back-brand .parent-name {
    color: #ffffff;
    font-size: 8px;
    transform: none;
    margin: 0 0 2px 118px;
  }
  .back-brand .brand-name { color: #ffffff; font-size: 26px; }

  .contact {
    position: absolute;
    left: 338px; top: 82px;
    font-size: 10.5px;
    line-height: 1.35;
    color: var(--ink);
  }
  .contact-name { font-size: 14px; font-weight: 700; color: var(--navy); }
  .contact-role { font-weight: 700; color: var(--orange); }
  .contact-company { font-weight: 700; color: #4f9fc0; margin-bottom: 8px; }
  .contact-label { color: var(--orange); }
</style>
</head>
<body>

  <section class="card card--front" aria-label="Card front">
    <div class="front-brand">
      <div class="brand-disc"></div>
      <div class="parent-name">TemaVista</div>
      <div class="brand-name">rotanokta</div>
    </div>
  </section>

  <section class="card card--back" aria-label="Card back">
    <svg class="back-panel" width="300" height="309" viewBox="0 0 300 309" aria-hidden="true">
      <path d="M0 0 H200 A190 190 0 0 1 200 309 H0 Z" fill="var(--navy)"/>
    </svg>
    <div class="back-brand">
      <div class="parent-name">TemaVista</div>
      <div class="brand-name">rotanokta</div>
    </div>

    <address class="contact" style="font-style: normal;">
      <div class="contact-name">Deniz Arslan</div>
      <div class="contact-role">Project manager</div>
      <div class="contact-company">TemaVista Turizm<br>ve Bilgi Teknolojileri A.Ş</div>
      <div>Address of company</div>
      <div>temavista.com</div>
      <div><span class="contact-label">p:</span> +90 212 555 0142</div>
      <div><span class="contact-label">e:</span> deniz.arslan@temavista.com</div>
    </address>
  </section>

</body>
</html>
```